CEO of company needs clear business card that stands out from the rest

I need a clear business card (standard credit card size) for the CEO/Founder of our company...Brightfield Counseling. We would like to see designs that use our logo colors, which are khaki, chocolate brown, and gray. The card should be an edgy design, maybe where half the card is transparent with curves on the card, or a textured card where the logo is transparent, I don't care much for white cards. The final design should communicate a funky, edgy, and modern look, as well as stand out to have the "WOW" factor. The information we need on the card would be Name, Title, Toll free number, Phone Number, address, email address, and website.

*PLEASE SEND FRONT AND BACK OF CARDS

Card is two sided front and back please give us your front and back designs

The card should be an edgy design, maybe where half the card is transparent with curves on the card, or a textured card where the logo is transparent, I don't care much for white cards. The final design should communicate a funky, edgy, and modern look, as well as stand out to have the "WOW" factor.

Please follow these guidelines for the card

SPECS (card):

2.125 (h) x 3.375 (w) card size after cut

2.375 (h) x 3.625 (w) card with bleed

300 dpi

cmyk

1/8 bleed

allow 1/8 border for live area

I will also attached the pdf for the information listed above which includes a diagram of the card

 

All the cards need to have rounded edges

I just updated a card as an example of how you can use different fonts on a single business card, look how the name is written in script, so what I am saying is make this a card you will be proud to design and put it in your portfolio 

Reason: this race is really close and I am working with 2 designers to fine tune their designs and the weekend is slowing us down

• Our Logo
MUST HAVE PARTS OF CARD THAT ARE TRANSPARENT. See ideas that are attached.
Card is two sided front and back
• The final design should communicate a funky, edgy, and modern look, as well as stand out to have the "WOW" factor. The information we need on the card would be Name, Title, Toll free number, Phone Number, address, email address, and website.

```html
<!DOCTYPE html>
<html lang="en">
<head>
<meta charset="utf-8">
<title>Brightfield Counseling – Business Card</title>
<link rel="stylesheet" href="https://fonts.googleapis.com/css2?family=PT+Sans:wght@400;700&display=swap">
<style>
  :root {
    --choc-center: #7b5330;
    --choc-edge: #693816;
    --khaki: #c9b89b;
    --khaki-soft: #bba98a;
    --gray: #9c9a98;
    --white: #ffffff;
  }
  * { margin: 0; padding: 0; box-sizing: border-box; }
  html, body { width: 1200px; height: 686px; overflow: hidden; }
  body { font-family: "PT Sans", Tahoma, sans-serif; }
  .card {
    position: relative;
    width: 1200px;
    height: 686px;
    background: radial-gradient(ellipse 60% 65% at 50% 55%, var(--choc-center) 0%, var(--choc-edge) 100%);
    overflow: hidden;
  }
  .header {
    position: absolute;
    top: 12px;
    left: 38px;
    display: flex;
    align-items: stretch;
  }
  .identity {
    width: 468px;
    display: flex;
    flex-direction: column;
    align-items: flex-end;
    padding-right: 12px;
  }
  .name {
    font-size: 58px;
    line-height: 58px;
    color: var(--khaki);
    white-space: nowrap;
  }
  .name .first { font-weight: 700; }
  .title {
    font-size: 52px;
    line-height: 54px;
    color: var(--gray);
    white-space: nowrap;
  }
  .divider {
    width: 3px;
    background: var(--khaki);
    margin: 2px 0 0;
  }
  .contact {
    padding-left: 12px;
    padding-top: 12px;
    color: var(--khaki);
  }
  .contact .email {
    font-size: 38px;
    line-height: 42px;
    white-space: nowrap;
  }
  .contact .phones {
    font-size: 35px;
    line-height: 38px;
    white-space: nowrap;
  }
  .contact .phones b { font-weight: 700; }
  .brand {
    position: absolute;
    left: 50%;
    top: 372px;
    transform: translate(-50%, -50%);
    display: flex;
    flex-direction: column;
    align-items: center;
    gap: 24px;
  }
  .brand-dot {
    width: 100px;
    height: 100px;
    border-radius: 50%;
    background: var(--white);
  }
  .brand-name {
    font-size: 56px;
    line-height: 62px;
    font-weight: 700;
    color: var(--white);
    text-align: center;
  }
  .footer {
    position: absolute;
    left: 0;
    right: 0;
    bottom: 12px;
    text-align: center;
    font-size: 39px;
    line-height: 44px;
    color: var(--khaki-soft);
    white-space: nowrap;
  }
</style>
</head>
<body>
  <div class="card">
    <header class="header">
      <div class="identity">
        <div class="name"><span class="first">Darren</span>Whitfield</div>
        <div class="title">Founder &amp; CEO</div>
      </div>
      <div class="divider"></div>
      <div class="contact">
        <div class="email">dwhitfield@brightfieldcounseling.com</div>
        <div class="phones"><b>t</b>.404.555.0182 <b>f</b>.678.555.0147</div>
      </div>
    </header>

    <div class="brand">
      <div class="brand-dot"></div>
      <div class="brand-name">Brightfield<br>Counseling</div>
    </div>

    <footer class="footer">toll free. 1.855.555.0136 | www.brightfieldcounseling.com</footer>
  </div>
</body>
</html>
```